Unique and original Business Card for Financial Services Business

I have moved premises and need to change the detail on my business card so thought now is a good time for a re-design. Looking for something professional and modern with colours to fit in with out logo. Like the idea of foil or embossing if that works but not a must have but I do want something that stands out and that I could not design myself.

Once business card is designed I will also be looking to get letterhead and flyers done but want the business card concept in place first.

The majority of designs I am receiving are generic and template based. I am looking for something unique and original. We have some great design elements in our logo, think outside the box and show me something that stands out from the crowd.

Target Market(s)

Business Professionals

Industry/Entity Type

Finance

Contact Information for Business Card

Name: Delia Norwood Phone 0473 958 162 Address PO Box 8617 Mossvale NSW 2389 Email info@steadyharbourfinancialservices.com.au website www.steadyharbourfinancialservices.com.au

Font styles to use
Other font styles liked:
• Ralway

Requirements
Should not have
• No black backgrounds please

```html
<!DOCTYPE html>
<html lang="en">
<head>
<meta charset="utf-8">
<title>Steady Harbour Financial Services – Business Card</title>
<link href="https://fonts.googleapis.com/css2?family=Raleway:wght@300;600&family=Encode+Sans+Condensed:wght@300&display=swap" rel="stylesheet">
<style>
  :root {
    --backdrop: #dadada;
    --card-navy: #053a58;
    --mint: #2fd08e;
    --mint-light: #35e38f;
    --teal-deep: #1a7f8a;
  }
  * { box-sizing: border-box; margin: 0; padding: 0; }
  html, body {
    width: 1200px; height: 846px; overflow: hidden;
    background: var(--backdrop);
  }
  .sheet { position: relative; width: 1200px; height: 846px; }
  .card {
    position: absolute; left: 346px; width: 508px; height: 290px;
    background: var(--card-navy);
    color: var(--mint);
  }
  .card--front { top: 99px; }
  .card--back { top: 457px; }

  .bird-artwork {
    position: absolute; left: 63px; top: 96px; width: 108px; height: 132px;
    background: linear-gradient(135deg, var(--mint-light) 0%, var(--mint) 45%, var(--teal-deep) 100%);
    border-radius: 46% 54% 40% 60% / 38% 42% 58% 62%;
    opacity: .9;
  }
  .holder-name {
    position: absolute; left: 215px; top: 90px;
    font-family: "Raleway", sans-serif; font-weight: 600; font-size: 15.5px;
    letter-spacing: .2px;
  }
  .contact-list { position: absolute; left: 188px; top: 126px; list-style: none; }
  .contact-item {
    display: flex; align-items: center; height: 22px;
    font-family: "Encode Sans Condensed", sans-serif; font-weight: 300; font-size: 13px;
  }
  .contact-icon { width: 18px; height: 18px; margin-right: 9px; fill: var(--mint); }

  .brand {
    position: absolute; left: 0; right: 0; top: 96px; text-align: center;
    font-family: "Raleway", sans-serif; font-weight: 300; color: var(--mint);
  }
  .brand-name { font-size: 37px; letter-spacing: -.3px; line-height: 1; }
  .brand-tagline { font-size: 19px; letter-spacing: 11.5px; margin-top: 6px; margin-left: 11px; }
</style>
</head>
<body>
<main class="sheet">
  <section class="card card--front">
    <div class="bird-artwork" role="img" aria-label="Illustration of a hummingbird in flight, mint to teal gradient"></div>
    <p class="holder-name">Delia Norwood</p>
    <ul class="contact-list">
      <li class="contact-item">
        <svg class="contact-icon" viewBox="0 0 24 24"><path d="M6.6 10.8a15 15 0 0 0 6.6 6.6l2.2-2.2c.3-.3.7-.4 1-.2 1.1.4 2.3.6 3.6.6.6 0 1 .4 1 1V20c0 .6-.4 1-1 1A17 17 0 0 1 3 4c0-.6.4-1 1-1h3.5c.6 0 1 .4 1 1 0 1.3.2 2.5.6 3.6.1.3 0 .7-.2 1z"/></svg>
        0473 958 162
      </li>
      <li class="contact-item">
        <svg class="contact-icon" viewBox="0 0 24 24"><path d="M2 5h20v14H2zm2 2v.4l8 5.4 8-5.4V7zm0 2.8V17h16V9.8l-8 5.4z"/></svg>
        info@steadyharbourfinancialservices.com.au
      </li>
      <li class="contact-item">
        <svg class="contact-icon" viewBox="0 0 24 24"><path d="M12 2a10 10 0 1 0 0 20 10 10 0 0 0 0-20zm6.9 6h-3a15 15 0 0 0-1.3-3.8A8 8 0 0 1 18.9 8zM12 4c.8 1.2 1.5 2.5 1.9 4h-3.8c.4-1.5 1.1-2.8 1.9-4zM4.3 14a8 8 0 0 1 0-4h3.4a16 16 0 0 0 0 4zm.8 2h3a15 15 0 0 0 1.3 3.8A8 8 0 0 1 5.1 16zm3-8h-3a8 8 0 0 1 4.3-3.8C8.8 5.4 8.4 6.7 8.1 8zM12 20c-.8-1.2-1.5-2.5-1.9-4h3.8c-.4 1.5-1.1 2.8-1.9 4zm2.3-6H9.7a14 14 0 0 1 0-4h4.6a14 14 0 0 1 0 4zm.3 5.8c.6-1.2 1-2.5 1.3-3.8h3a8 8 0 0 1-4.3 3.8zm1.7-5.8a16 16 0 0 0 0-4h3.4a8 8 0 0 1 0 4z"/></svg>
        www.steadyharbourfinancialservices.com.au
      </li>
      <li class="contact-item">
        <svg class="contact-icon" viewBox="0 0 24 24"><path d="M12 1a6 6 0 0 0-6 6c0 4.5 6 11 6 11s6-6.5 6-11a6 6 0 0 0-6-6zm0 8.2A2.2 2.2 0 1 1 12 4.8a2.2 2.2 0 0 1 0 4.4zM5 19.5c0-1 1.6-1.9 4-2.3l.9 1.1c-1.9.2-3.1.7-3.1 1.2 0 .7 2.4 1.3 5.2 1.3s5.2-.6 5.2-1.3c0-.5-1.2-1-3.1-1.2l.9-1.1c2.4.4 4 1.3 4 2.3 0 1.6-3.1 2.7-7 2.7s-7-1.1-7-2.7z"/></svg>
        PO Box 8617 Mossvale NSW 2389
      </li>
    </ul>
  </section>

  <section class="card card--back">
    <div class="brand">
      <p class="brand-name">STEADY HARBOUR</p>
      <p class="brand-tagline">Financial Services</p>
    </div>
  </section>
</main>
</body>
</html>
```